Bluegull Harbor Tours and Charters

I'm looking to update my current website that was written in Joomla. I would like to move to a more modern design that works well on all platforms using a Wordpress theme. The website is, https://www.bluegullharbortours.example/ It should be noted that I currently have an online booking API (Tidebook) that is integrated with the site but I don't want to worry about that for now. Once I get the new site up and running I am going to move to Quayly which doesn't hook into the site, it just links to an external booking company. Just ignore the Tidebook booking (Book Now) code and build the site. IMPORTANT: My website is hosted on HostMarlow and I currently manage it through cPanel. I want to be able to make changes, updates and manage the website once its completed.

Target Market(s)

Tourists visiting Siesta Key and Venice Florida for Dolphin, sunset tours and private half and full day charters to Pelican Rib Island.

Industry/Entity Type

Tourism

Coding

Coded - Design and coding required

Font styles to use
Other font styles liked:
• Freebooter

Colors
0455a3
85acd3
fbed22
fbee3e
ffc214
ffcf3e
f78f20
faa54b

Requirements
Must have
• Our brand is fun on the water. Social Media links. Great photos, we will provide, and compelling descriptions of each of the tours we offer.
• Dolphin Tours
• Sunset Tours
• Shelling and Snorkeling
• Boating Instruction - I would like this page to have a more professional look and feel. It needs to stand out from the other pages as a professional service yet it still needs to blend well with the entire site.
• What can you do to make this site, https://www.bluegullharbortours.example/ better?
• I don't really need a "Gallery Page" but I want to highlight lots of great pics from our tours. Here is a good example..... check this site out.
• https://brindlecharters.example/
• I don't want to be "like" Brindle Charters, I want my site to be better. This is my competitor.
Nice to have
• I selected some colors for the theme but basically I just want it to be a bright, fun and outgoing site.
• There is a font you can download called Freebooter. It gives it that Pirate look and feel. I would like to use that in some places. Its in my logo on the website. Don't go overboard with the Pirate look and feel but some subtitle pirate things in the site would make it fun.

```html
<!DOCTYPE html>
<html lang="en">
<head>
<meta charset="utf-8">
<title>Bluegull Harbor Tours and Charters</title>
<link href="https://fonts.googleapis.com/css2?family=Montserrat:wght@600;700;800&family=Open+Sans:wght@400;600;700&family=Great+Vibes&display=swap" rel="stylesheet">
<style>
:root{
  --blue:#0455a3;
  --sky:#85acd3;
  --panel:#7ea3d0;
  --yellow:#ffc214;
  --yellow-soft:#ffcf3e;
  --orange:#f78f20;
  --ink:#2b2b2b;
  --muted:#777;
  --line:#e3e3e3;
  --dark:#1c1f26;
  --white:#fff;
}
*{box-sizing:border-box;margin:0;padding:0}
html,body{width:1200px;height:3428px;overflow:hidden}
body{font-family:"Open Sans",Arial,sans-serif;color:var(--ink);background:var(--white);position:relative}
.script{font-family:"Great Vibes",cursive;font-size:30px;color:#555;text-align:center}
.heading{font-family:"Montserrat",Arial,sans-serif;font-weight:800;font-size:32px;text-align:center;color:#222;letter-spacing:.5px}
.rule{display:flex;justify-content:center;gap:6px;margin:12px auto 0}
.rule span{height:3px;width:26px;background:var(--yellow)}
.rule span:nth-child(2){width:8px;background:var(--orange)}
.btn{display:inline-block;background:var(--yellow);color:var(--white);font-family:"Montserrat",Arial,sans-serif;font-weight:700;font-size:14px;letter-spacing:.5px;padding:12px 26px;text-transform:uppercase}
.photo{display:block}

/* header */
.site-header{position:absolute;top:0;left:0;width:1200px;height:112px;background:var(--white);display:flex;align-items:center;padding:0 60px}
.brand{display:flex;align-items:center;gap:10px;width:300px}
.brand-dot{width:34px;height:34px;border-radius:50%;background:var(--yellow)}
.brand-name{font-family:"Montserrat",Arial,sans-serif;font-weight:700;font-size:15px;color:var(--blue);line-height:1.2;width:170px}
.main-nav{display:flex;gap:34px;font-size:15px;color:#444;margin-left:120px}
.call-btn{position:absolute;right:60px;top:0;background:var(--sky);color:var(--white);font-family:"Montserrat",Arial,sans-serif;font-weight:700;font-size:15px;padding:14px 24px}

/* hero */
.hero{position:absolute;top:112px;left:0;width:1200px;height:668px;background:linear-gradient(180deg,#2a3447 0%,#6a4a3a 40%,#d9822b 62%,#3a2a24 75%,#1f2430 100%)}
.hero-copy{position:absolute;top:250px;width:100%;text-align:center;color:var(--white)}
.hero-copy .script{color:var(--white);font-size:32px}
.hero-title{font-family:"Montserrat",Arial,sans-serif;font-weight:800;font-size:64px;letter-spacing:1px;margin:6px 0 22px}
.hero-title em{font-style:normal;color:var(--yellow)}
.booking-bar{position:absolute;top:660px;left:120px;width:960px;height:84px;background:var(--white);box-shadow:0 6px 20px rgba(0,0,0,.15);display:flex;align-items:center;gap:16px;padding:0 20px}
.field{flex:1;height:40px;border:1px solid var(--line);font-size:13px;color:#888;display:flex;align-items:center;justify-content:space-between;padding:0 12px}
.field svg{width:10px;height:10px}
.booking-bar .btn{padding:12px 30px}

/* why */
.why{position:absolute;top:820px;left:0;width:1200px;height:500px}
.why-sail{position:absolute;right:0;top:40px;width:150px;height:420px;background:linear-gradient(180deg,#eef3f8,#c9d6e3)}
.cards{position:absolute;top:70px;left:130px;display:flex;gap:34px}
.card{width:290px;height:410px;background:var(--white);box-shadow:0 4px 18px rgba(0,0,0,.12);padding:20px;text-align:center}
.card .photo{height:120px;margin-bottom:16px}
.card h3{font-family:"Montserrat",Arial,sans-serif;font-weight:800;font-size:17px;margin-bottom:10px}
.card p{font-size:12.5px;color:var(--muted);line-height:1.6;text-align:left;margin-bottom:18px;height:120px}
.card .btn{padding:10px 26px;font-size:13px}

/* about */
.about{position:absolute;top:1360px;left:0;width:1200px;height:480px}
.about-aerial{position:absolute;left:0;top:0;width:520px;height:480px;background:linear-gradient(135deg,#1f5a4a,#2d7a8a 50%,#9bb8c0)}
.about-sunset{position:absolute;left:180px;top:170px;width:330px;height:220px;background:linear-gradient(180deg,#7b3a8a,#d05a7a 55%,#2a2f5a);border:6px solid var(--white)}
.play{position:absolute;left:325px;top:260px}
.about-panel{position:absolute;left:520px;top:30px;width:680px;height:400px;background:var(--panel);padding:40px 60px;color:var(--white)}
.about-panel .script{color:var(--white);text-align:left;font-size:28px}
.about-panel .heading{color:var(--white);text-align:left}
.about-panel .rule{justify-content:flex-start;margin:10px 0 18px}
.about-panel p{font-size:13px;line-height:1.7;margin-bottom:10px}

/* services */
.services{position:absolute;top:1890px;left:0;width:1200px;height:620px}
.cols{position:absolute;top:140px;left:130px;display:flex;gap:34px}
.col{width:290px;height:460px;background:var(--white);box-shadow:0 4px 18px rgba(0,0,0,.1)}
.col .photo{height:200px}
.col-body{padding:22px}
.col h3{font-family:"Montserrat",Arial,sans-serif;font-weight:800;font-size:17px;margin-bottom:12px}
.col ul{list-style:none;font-size:13px;color:var(--muted);line-height:1.9}
.col li::before{content:"";display:inline-block;width:6px;height:6px;background:var(--yellow);border-radius:50%;margin-right:8px;vertical-align:middle}
.col p{font-size:13px;color:var(--muted);line-height:1.7}

/* gallery */
.gallery{position:absolute;top:2550px;left:0;width:1200px;height:260px}
.strip{position:absolute;top:130px;left:0;width:1200px;height:120px;display:flex}
.strip .photo{flex:1;height:120px}

/* cta */
.cta{position:absolute;top:2850px;left:0;width:1200px;height:340px;background:linear-gradient(160deg,#2f6e6a,#5b9aa8 45%,#9cc3c9 70%,#3b6d6f);text-align:center;color:var(--white)}
.cta .script{color:var(--white);padding-top:80px}
.cta-title{font-family:"Montserrat",Arial,sans-serif;font-weight:800;font-size:50px;margin:4px 0 22px}
.cta-title em{font-style:normal;color:var(--yellow)}

/* footer */
.site-footer{position:absolute;top:3200px;left:0;width:1200px;height:192px;background:var(--dark);color:var(--white);display:flex;align-items:center;padding:0 80px}
.site-footer .brand-name{color:var(--white)}
.foot-call{margin-left:120px;width:400px}
.foot-call h4{font-family:"Montserrat",Arial,sans-serif;font-weight:700;font-size:20px;margin-bottom:8px}
.foot-call p{font-size:12px;color:#bbb;line-height:1.6}
.gift{margin-left:60px}
.gift h4{font-family:"Montserrat",Arial,sans-serif;font-weight:700;font-size:18px;margin-bottom:12px}
.bottom-bar{position:absolute;top:3392px;left:0;width:1200px;height:36px;background:#111318;color:#999;font-size:11px;display:flex;align-items:center;justify-content:space-between;padding:0 80px}
</style>
</head>
<body>

<header class="site-header">
  <div class="brand"><span class="brand-dot"></span><span class="brand-name">Bluegull Harbor Tours and Charters</span></div>
  <nav class="main-nav"><span>Home</span><span>Tour Info</span><span>Select a Tour</span><span>Boating Instruction</span><span>Gallery</span><span>Contact</span></nav>
  <div class="call-btn">CALL NOW : 941-555-0148</div>
</header>

<section class="hero" role="img" aria-label="Sailboat silhouetted on the water at sunset">
  <div class="hero-copy">
    <div class="script">Be fearless in the pursuit of what sets your soul on fire</div>
    <h1 class="hero-title">ADVENTURE IS <em>WORTHWHILE</em></h1>
    <span class="btn">View Charter</span>
  </div>
</section>

<form class="booking-bar">
  <div class="field">Tour List <svg viewBox="0 0 10 10"><path d="M1 3l4 4 4-4" fill="none" stroke="#999" stroke-width="1.5"/></svg></div>
  <div class="field">Date <svg viewBox="0 0 10 10"><rect x="1" y="2" width="8" height="7" fill="none" stroke="#999"/></svg></div>
  <div class="field">Adults</div>
  <div class="field">Child</div>
  <span class="btn">Book Now</span>
</form>

<section class="why">
  <div class="why-sail photo" role="img" aria-label="White sailboat on the bay"></div>
  <div class="script">Explore a different way of travel</div>
  <h2 class="heading">WHY CHOOSE US</h2>
  <div class="rule"><span></span><span></span><span></span></div>
  <div class="cards">
    <article class="card">
      <div class="photo" role="img" aria-label="Dolphin surfacing in blue water" style="background:linear-gradient(180deg,#3d8fb0,#1d5f7f)"></div>
      <h3>DOLPHIN TOURS</h3>
      <p>Glide across calm bay waters while playful bottlenose dolphins ride the wake beside our boat. Our captains know every favorite feeding spot along the coast.</p>
      <span class="btn">Book Now</span>
    </article>
    <article class="card">
      <div class="photo" role="img" aria-label="Sunset over the Gulf" style="background:linear-gradient(180deg,#f4a23a,#d8642a 55%,#3a3550)"></div>
      <h3>SUNSET TOURS</h3>
      <p>Settle in as the sky turns gold and crimson over the Gulf. A relaxed evening cruise with cold drinks, soft music and unforgettable views.</p>
      <span class="btn">Book Now</span>
    </article>
    <article class="card">
      <div class="photo" role="img" aria-label="Seashell on the sand" style="background:linear-gradient(180deg,#d9cfc2,#b8a48e)"></div>
      <h3>SHELLING &amp; SNORKLING</h3>
      <p>Wade the shallow flats of Pelican Rib Island for shells and sand dollars, then snorkel clear water full of fish, rays and sea grass.</p>
      <span class="btn">Book Now</span>
    </article>
  </div>
</section>

<section class="about">
  <div class="about-aerial photo" role="img" aria-label="Aerial view of a marina with boats"></div>
  <div class="about-sunset photo" role="img" aria-label="Pink and purple sunset over the water"></div>
  <svg class="play" width="40" height="40" viewBox="0 0 40 40"><circle cx="20" cy="20" r="18" fill="none" stroke="#fff" stroke-width="2"/><path d="M16 12l12 8-12 8z" fill="#fff"/></svg>
  <div class="about-panel">
    <div class="script">Book your vacation with us</div>
    <h2 class="heading">ABOUT US</h2>
    <div class="rule"><span></span><span></span><span></span></div>
    <p>Our family-run crew has been sharing the Gulf Coast with visitors for years. Every trip is small, friendly and led by licensed captains who love these waters as much as you will.</p>
    <p>From dolphin watching to private island getaways, we tailor each charter to your group. Bring your camera, your sense of adventure and leave the rest to us.</p>
  </div>
</section>

<section class="services">
  <div class="script">About Our Boat Services</div>
  <h2 class="heading">DOLPHINS, SIGHTSEEING &amp; SUNSET TOURS!</h2>
  <div class="rule"><span></span><span></span><span></span></div>
  <div class="cols">
    <article class="col">
      <div class="photo" role="img" aria-label="Tropical beach with palm trees" style="background:linear-gradient(180deg,#6cb3e0,#4aa2a0 60%,#e8dcc0)"></div>
      <div class="col-body"><h3>TOURS</h3>
        <ul><li>Hourly Tours</li><li>Island Hopping</li><li>Sightseeing</li><li>Sunset Tours</li><li>Boat Rides</li><li>Visit your favorite beach spot</li></ul></div>
    </article>
    <article class="col">
      <div class="photo" role="img" aria-label="Charter boat deck on open water" style="background:linear-gradient(180deg,#9cc4e4,#e9eef2 55%,#7aa0b8)"></div>
      <div class="col-body"><h3>CHARTERS</h3>
        <ul><li>Full Day Charter</li><li>Half Day Charters</li><li>Private Charters</li><li>Multi Island Hopping</li><li>Fishing</li></ul></div>
    </article>
    <article class="col">
      <div class="photo" role="img" aria-label="Captain at the helm of a boat" style="background:linear-gradient(180deg,#b9d6ee,#eef2f5 60%,#5f89a6)"></div>
      <div class="col-body"><h3>SERVICES</h3>
        <p>Tour packages are planned around tide and weather so every outing on the water is safe, smooth and fun.</p></div>
    </article>
  </div>
</section>

<section class="gallery">
  <div class="script">See and enjoy all moments of fun with</div>
  <h2 class="heading">GALLERY FROM MEMBERS</h2>
  <div class="rule"><span></span><span></span><span></span></div>
  <div class="strip">
    <div class="photo" role="img" aria-label="Guests on a boat tour" style="background:#6f8fa6"></div>
    <div class="photo" role="img" aria-label="Boat on the water" style="background:#4d7f9c"></div>
    <div class="photo" role="img" aria-label="Guests holding shells" style="background:#c9a46a"></div>
    <div class="photo" role="img" aria-label="Sunset cruise" style="background:#d48a4a"></div>
    <div class="photo" role="img" aria-label="Island beach" style="background:#7fb3c2"></div>
    <div class="photo" role="img" aria-label="Captain and guests" style="background:#5d8a98"></div>
    <div class="photo" role="img" aria-label="Snorkeling in clear water" style="background:#3f91a8"></div>
    <div class="photo" role="img" aria-label="Family on deck" style="background:#9aa9b6"></div>
  </div>
</section>

<section class="cta" role="img" aria-label="Aerial view of boats anchored off a sandbar">
  <div class="script">Ready to Sail Away</div>
  <h2 class="cta-title">SELECT A CHARTER TO <em>GET STARTED</em></h2>
  <span class="btn">View Charter</span>
</section>

<footer class="site-footer">
  <div class="brand"><span class="brand-dot"></span><span class="brand-name">Bluegull Harbor Tours and Charters</span></div>
  <div class="foot-call">
    <h4>CALL NOW! 941-555-0148</h4>
    <p>Consider booking on our website or call our friendly team. Follow us for daily updates and photos.</p>
  </div>
  <div class="gift">
    <h4>GIFTS CARDS AVAILABLE</h4>
    <span class="btn">Purchase</span>
  </div>
</footer>
<div class="bottom-bar"><span>Copyright © 2024. All rights reserved.</span><span>Find us on social media</span></div>

</body>
</html>
```